Free Range Egg Farmer wants a Egg Carton Design

We need a design for Free Range Egg carton. Our company name is "BrookHaven The Craft of Growing"

We run a environmentally friendly farm in Gippsland VIC and we produce Free Range Eggs and Pasture Fed Meats in open pasture.

We also run a farm stay business in a very high energy star rating house.
The farm guest participates in our farm activity such as looking after farm animals, maintaining the vegetable garden, cooking fresh food, Yoga and Meditation.

We would like to see designs with our logo and something alternative rather than a typical free range egg cartons.

The team had a meeting and came up with one idea.
"The meditating hen" with thought bubble which we can change the hen's thought by printing batch.
You could either use this idea or create your own.

I have attached 3 photos close to my image as examples.
I also have attached the typical free range egg cartons as examples.

Sticker size is attached. The sticker fits between the case closure system. So there is no need to make spaces for the closure gaps.
Please place Best Before stamp area at the top right corner of the main (middle) section.
Updates

I have post an update to my brief. Please have a look again. BrookHaven

Industry/Entity Type

Printing

Requirements
Must have
• Company name,
Address,
contact number,
facebook logo,
best before date (space to put the stamp on)
12 Free Range Eggs xxx g
Nutrition info

```html
<!DOCTYPE html>
<html lang="en">
<head>
<meta charset="utf-8">
<title>BrookHaven Free Range Egg Carton Sticker</title>
<link href="https://fonts.googleapis.com/css2?family=Alike&family=Roboto+Condensed:wght@400;700&display=swap" rel="stylesheet">
<style>
  :root{
    --stage:#2b2826;
    --red:#e3262b;
    --red-deep:#c9252b;
    --orange:#f08a2e;
    --orange-soft:#f6a640;
    --yellow:#fdd21a;
    --yellow-light:#fff59a;
    --brown:#9c5224;
    --brown-dark:#6b2d1c;
    --ground:#b8692c;
    --ink:#2a2a2a;
    --white:#ffffff;
    --seal:#3b3a3a;
  }
  *{margin:0;padding:0;box-sizing:border-box}
  html,body{width:1200px;height:1000px;overflow:hidden;background:var(--stage)}
  .canvas{position:relative;width:1200px;height:1000px;background:var(--stage);font-family:"Roboto Condensed",Arial,sans-serif}
  .panel{position:absolute;left:87px;width:1033px;overflow:hidden}
  .panel > svg.bg{position:absolute;inset:0;width:100%;height:100%}
  .panel--lid-back{top:45px;height:193px}
  .panel--main{top:255px;height:483px;background:linear-gradient(90deg,#e8503a 0%,#f28a3a 35%,#f9b42a 65%,var(--yellow) 100%)}
  .panel--lid-front{top:755px;height:193px}
  .flipped{position:absolute;inset:0;transform:rotate(180deg)}
  .seal{position:absolute;border-radius:50%;background:var(--seal);border:3px solid #d9d9d9}
  .brand-name{position:absolute;color:var(--white);font-weight:700;font-size:14px;line-height:18px;text-align:center;white-space:nowrap;transform:translateX(-50%)}
  .strip-title{position:absolute;font-family:"Alike",Georgia,serif;font-size:54px;color:var(--white);white-space:nowrap;transform:translate(-50%,-50%);
    -webkit-text-stroke:5px var(--brown-dark);paint-order:stroke fill;text-shadow:2px 2px 0 rgba(90,30,10,.35)}
  .nutrition{position:absolute;left:770px;top:25px;width:224px;height:136px;border:1px solid var(--ink);padding:34px 8px 0 8px;font-size:11.5px;line-height:17px;color:var(--ink)}
  .nutrition__head{position:absolute;left:-1px;top:-1px;width:94px;height:22px;border:1px solid var(--ink);font-size:11.5px;line-height:20px;padding-left:5px}
  .hen{position:absolute;left:290px;top:195px;width:190px;height:215px;border-radius:45% 40% 20% 20%;background:radial-gradient(circle at 50% 40%,#ffffff 0%,#eeeeee 70%,#d8d8d8 100%)}
  .egg-pile{position:absolute;left:0;top:412px;width:1033px;height:71px;background:linear-gradient(180deg,#f7c93a 0%,#f5b12c 55%,#ec8b25 100%)}
  .badge-title{position:absolute;left:474px;top:74px;width:268px;height:268px;border-radius:50%;background:linear-gradient(90deg,var(--yellow-light) 0%,#ffee3a 55%,#ffe400 100%);box-shadow:0 6px 16px rgba(120,50,0,.25)}
  .badge-title::after{content:"";position:absolute;inset:12px;border-radius:50%;border:2px solid var(--orange)}
  .badge-title__text{position:absolute;inset:0;display:flex;flex-direction:column;align-items:center;justify-content:center;font-family:"Alike",Georgia,serif;color:var(--red);font-size:62px;line-height:60px;text-align:center}
  .bubble{position:absolute;border-radius:50%;background:radial-gradient(circle at 40% 40%,#ffe95a,#fbbd1a);border:3px solid #f07a30}
  .count-tag{position:absolute;left:880px;top:118px;width:120px;height:120px}
  .count-tag__text{position:absolute;left:855px;top:145px;width:130px;text-align:center;color:var(--red);font-weight:700;font-size:14px;line-height:15px}
  .count-tag__text .first{font-size:16px;line-height:20px}
  .count-tag__weight{display:block;margin:4px auto 0;width:70px;border-top:1.5px solid var(--red);color:var(--ink);font-size:12px;padding-top:3px}
  .best-before{position:absolute;left:838px;top:258px;width:164px;height:164px}
  .best-before__label{position:absolute;left:880px;top:300px;width:80px;text-align:center;color:var(--red);font-weight:700;font-size:10px;border-bottom:1.5px solid var(--red);padding-bottom:2px}
  .contact{position:absolute;left:806px;top:60px;height:78px;border-left:1px solid #7a4a20;padding-left:20px;font-size:12px;line-height:17px;color:#3a2a1a;padding-top:0}
  .contact p{white-space:nowrap}
  .social-square{display:inline-block;width:12px;height:12px;background:#3b5998;vertical-align:-2px;margin-right:3px}
</style>
</head>
<body>
<div class="canvas">

  <!-- Lid back strip (printed upside down) -->
  <section class="panel panel--lid-back">
    <svg class="bg" viewBox="0 0 1033 193" preserveAspectRatio="none" aria-hidden="true">
      <defs>
        <linearGradient id="lidBackBase" x1="0" x2="1" y1="0" y2="0">
          <stop offset="0" stop-color="#fdd51c"/><stop offset=".5" stop-color="#f49a35"/><stop offset="1" stop-color="#e6463a"/>
        </linearGradient>
      </defs>
      <rect width="1033" height="193" fill="url(#lidBackBase)"/>
      <path d="M0 40 C200 90 380 10 600 35 C780 55 900 20 1033 0 L1033 0 L0 0Z" fill="#f08a2e" opacity=".75"/>
      <path d="M600 0 C760 40 880 10 1033 60 L1033 0Z" fill="#d8332e" opacity=".8"/>
      <path d="M0 193 C200 150 420 190 700 165 C860 150 960 170 1033 160 L1033 193Z" fill="#f7b22c" opacity=".6"/>
    </svg>
    <div class="flipped">
      <div class="seal" style="left:72px;top:37px;width:82px;height:82px"></div>
      <div class="brand-name" style="left:113px;top:124px;font-size:12px;line-height:15px">BrookHaven<br>The Craft of Growing</div>
      <div class="strip-title" style="left:470px;top:98px">Free Range Egg</div>
      <div class="nutrition">
        <div class="nutrition__head">Nutrition info</div>
        <p>Energy 310kJ, protein 6.3g, fat 5.1g per egg.</p>
        <p>Saturated fat 1.6g, carbohydrate 0.3g, sugars 0.2g.</p>
        <p>Sodium 62mg, cholesterol 186mg, vitamin D 0.9µg</p>
        <p>Store below 5°C in a dry place.</p>
      </div>
    </div>
  </section>

  <!-- Main lid panel -->
  <section class="panel panel--main">
    <svg class="bg" viewBox="0 0 1033 483" preserveAspectRatio="none" aria-hidden="true">
      <path d="M0 335 C120 300 220 285 330 290 C430 292 520 310 600 330 C700 300 820 290 940 310 C990 318 1020 330 1033 335 L1033 483 L0 483Z" fill="#b56530" opacity=".55"/>
      <path d="M0 350 C140 320 260 300 380 310 C480 318 560 345 640 360 C760 370 900 360 1033 375 L1033 483 L0 483Z" fill="#9c5224"/>
      <path d="M0 365 C200 360 420 362 640 368 C800 372 940 378 1033 380 L1033 483 L0 483Z" fill="#b8692c"/>
    </svg>

    <div class="seal" style="left:60px;top:50px;width:100px;height:100px"></div>
    <div class="brand-name" style="left:110px;top:158px">BrookHaven<br>The Craft of Growing</div>

    <div class="hen" role="img" aria-label="Illustration of a white hen standing in the field, looking up at its thought bubbles"></div>

    <div class="bubble" style="left:364px;top:143px;width:26px;height:26px"></div>
    <div class="bubble" style="left:386px;top:80px;width:48px;height:48px"></div>
    <div class="bubble" style="left:444px;top:55px;width:62px;height:62px"></div>

    <div class="badge-title">
      <div class="badge-title__text"><span>Free</span><span>Range</span><span>Egg</span></div>
    </div>

    <svg class="count-tag" viewBox="0 0 120 120" aria-hidden="true" style="left:862px;top:112px;width:150px;height:150px">
      <rect x="22" y="22" width="76" height="76" transform="rotate(45 60 60)" fill="#ffffff" stroke="#e3262b" stroke-width="6"/>
      <rect x="28" y="28" width="64" height="64" transform="rotate(45 60 60)" fill="none" stroke="#e3262b" stroke-width="1"/>
    </svg>
    <div class="count-tag__text" style="left:872px;top:148px">
      <span class="first">12</span><br>Free Range<br>Eggs
      <span class="count-tag__weight">700 g</span>
    </div>

    <svg class="best-before" viewBox="0 0 164 164" aria-hidden="true">
      <polygon fill="#e3262b" points="82,2 93,14 108,6 114,21 131,19 131,35 147,40 140,55 153,66 141,77 150,91 136,98 141,114 125,118 126,135 110,134 104,150 90,143 82,158 74,143 60,150 54,134 38,135 39,118 23,114 28,98 14,91 23,77 11,66 24,55 17,40 33,35 33,19 50,21 56,6 71,14"/>
      <circle cx="82" cy="80" r="62" fill="#f6a640"/>
      <circle cx="82" cy="80" r="56" fill="#ffffff" stroke="#e3262b" stroke-width="2"/>
    </svg>
    <div class="best-before__label" style="left:880px;top:300px">BEST BEFORE</div>

    <div class="egg-pile" role="img" aria-label="Illustration of a field of golden eggs along the bottom edge"></div>
  </section>

  <!-- Lid front strip -->
  <section class="panel panel--lid-front">
    <svg class="bg" viewBox="0 0 1033 193" preserveAspectRatio="none" aria-hidden="true">
      <defs>
        <linearGradient id="lidFrontBase" x1="0" x2="1" y1="0" y2="0">
          <stop offset="0" stop-color="#e6463a"/><stop offset=".5" stop-color="#f49a35"/><stop offset="1" stop-color="#fdd51c"/>
        </linearGradient>
      </defs>
      <rect width="1033" height="193" fill="url(#lidFrontBase)"/>
      <path d="M0 110 C160 60 330 140 520 110 C700 80 860 120 1033 90 L1033 193 L0 193Z" fill="#f08a2e" opacity=".7"/>
      <path d="M0 140 C160 110 300 170 480 150 C620 135 700 170 800 193 L0 193Z" fill="#d33a2e" opacity=".85"/>
      <path d="M0 0 L0 40 C200 10 420 60 640 20 C760 0 900 30 1033 10 L1033 0Z" fill="#fbc02a" opacity=".35"/>
    </svg>
    <div class="seal" style="left:73px;top:43px;width:80px;height:80px"></div>
    <div class="brand-name" style="left:113px;top:130px;font-size:12.5px;line-height:15px">BrookHaven<br>The Craft of Growing</div>
    <div class="strip-title" style="left:498px;top:95px">Free Range Egg</div>
    <div class="contact">
      <p>Address, 42 Ridge Road,</p>
      <p>Mirboo North VIC 3871.</p>
      <p>0355 010 482</p>
      <p><span class="social-square"></span>facebook.com/brookhavenfarm</p>
    </div>
  </section>

</div>
</body>
</html>
```